3D Video Animation – Sorelle Edit PMU Pigments

About Sorelle Edit PMU Pigments

Aqua-based formula: Fluid consistency that allows for smooth application and optimal absorption.
Vibrant, long-lasting colors: Fade-resistant and perfect for various PMU procedures like eyebrow micropigmentation, lip blush, and eyeliner tattoos.
High quality & safety: The formula contains no harmful or irritating compounds.
Inspired by water: The colors and texture evoke a sense of purity, freshness, and fluidity.
Optimal Flow: Ensures smooth and even pigment distribution.
Skin Types: Pigments are suitable for all skin types.
Standards: Pigments are carefully crafted to meet all EU REACH standards

What is a PMU?

PMU (Permanent Makeup) is a cosmetic procedure where pigment is implanted into the skin using specialized equipment to mimic the look of makeup.
It is commonly used for eyebrows, eyeliner, and lip tattoos.

Project Requirements

Video Length: 10 seconds
Style: 3D animation, dynamic, colorful, high-energy
Key Focus: Aqua-themed movement, smooth flow, and energetic visuals.
Brand Aesthetic: Modern, premium, and visually engaging.

Technical Details

Resolution: 9:16 (1080x1920)
Format: MP4
Frame Rate: 24fps
Sound: Optional, but a subtle, elegant background sound is encouraged.

Judging Criteria

Creativity & originality
Smoothness of animation and transitions
High-quality rendering and attention to detail
Alignment with the Sorelle Edit theme
Overall visual appeal and impact
Updates

Low design quality

Target Market(s)

Makeup artists, PMU artist, beauty salons

Industry/Entity Type

Beauty industry

Font styles to use
Sans Serif

Colors
0054AA
0677BA
7BADD7
CADEEF
E8F1F8
0094D4
00A9DD
6FCCEA
C7EBF8
E9F6FB
00AB8E
00BBA5
67D7C9
C6EFE9
E9F9F6

Requirements
Must have
• Product photos - bottles

```html
<!DOCTYPE html>
<html lang="en">
<head>
<meta charset="utf-8">
<title>PMU Ink</title>
<link rel="stylesheet" href="https://fonts.googleapis.com/css2?family=Montserrat:wght@800;900&display=swap">
<style>
  :root {
    --page-bg: #ffffff;
    --poster-teal: #14b8b4;
    --text-white: #ffffff;
    --bottle-cap-top: #1d6f74;
    --bottle-cap-bottom: #1f8488;
    --bottle-body: #c2733c;
    --bottle-base: #a65a2a;
    --bottle-label: #9fd3cf;
  }
  * { margin: 0; padding: 0; box-sizing: border-box; }
  html, body {
    width: 1200px;
    height: 1000px;
    overflow: hidden;
    background: var(--page-bg);
  }
  .canvas {
    position: relative;
    width: 1200px;
    height: 1000px;
    background: var(--page-bg);
  }
  .poster {
    position: absolute;
    left: 360px;
    top: 72px;
    width: 481px;
    height: 856px;
    background: var(--poster-teal);
    overflow: hidden;
    font-family: "Montserrat", sans-serif;
    color: var(--text-white);
  }
  .product-bottle {
    position: absolute;
    left: 130px;
    top: 258px;
    width: 223px;
    height: 575px;
  }
  .bottle-cap {
    position: absolute;
    left: 30px;
    top: 0;
    width: 163px;
    height: 280px;
    border-radius: 40px 40px 10px 10px;
    background: linear-gradient(to bottom, var(--bottle-cap-top), var(--bottle-cap-bottom));
  }
  .bottle-body {
    position: absolute;
    left: 0;
    top: 275px;
    width: 223px;
    height: 300px;
    border-radius: 30px 30px 24px 24px;
    background: linear-gradient(to bottom, var(--bottle-body), var(--bottle-base));
  }
  .bottle-label {
    position: absolute;
    left: 4px;
    top: 42px;
    width: 215px;
    height: 210px;
    background: var(--bottle-label);
    opacity: 0.85;
  }
  .headline {
    position: absolute;
    left: 74px;
    top: 18px;
    font-weight: 900;
    font-size: 146px;
    line-height: 146px;
    letter-spacing: -5px;
  }
  .feature-list {
    position: absolute;
    left: 80px;
    font-weight: 800;
    font-size: 44px;
    line-height: 58px;
    letter-spacing: 8px;
  }
  .feature-list.uses { top: 348px; }
  .feature-list.qualities { top: 588px; }
  .feature-list span { display: block; }
</style>
</head>
<body>
  <div class="canvas">
    <section class="poster">
      <div class="product-bottle" role="img" aria-label="3D render of a PMU pigment bottle with teal dropper cap, warm brown body and pale aqua label">
        <div class="bottle-cap"></div>
        <div class="bottle-body"><div class="bottle-label"></div></div>
      </div>
      <h1 class="headline">PMU<br>Ink</h1>
      <p class="feature-list uses">
        <span>Lips</span>
        <span>Eyebrows</span>
        <span>Eyeliner</span>
      </p>
      <p class="feature-list qualities">
        <span>Painless</span>
        <span>Pure</span>
        <span>Natural</span>
      </p>
    </section>
  </div>
</body>
</html>
```